Design Book Cover for PhD Thesis on Cryptanalysis

I need a book cover design (front, back & spine) for my PhD thesis called "Pathways through Lattice Ciphers and Their Uses".
Author: Joost Verhagel
Keywords: cryptanalysis, digital fingerprint, digital signature, digital certificate, collision of fingerprint/signature, bit-difference.
The finished book will have dimensions 17cm by 24cm by ?cm.
The (flat-)spine thickness is yet unknown, but will probably be about 1cm.
The cover design thus needs from left-to-right:
- a back of 17cm by 24cm
- in between a spine of about 1cm by 24cm
- a front of 17cm by 24cm
Around this design a 3mm bleeding/cutoff edge is needed
(leading to a total height of 24.6 cm and total width of 35.6cm).
The spine-fold is located 7mm from the spine on the front and back cover,
so the title etc. should be removed at least 1cm from the spine.
Below I will provide a description of my biggest results in my thesis and try to give some idea of the techniques used, which may help you for inspiration.
As you will read below, cryptanalysis comes close to "hacking".
However, cryptanalysis involves much more mathematics, and our goal is to provide recommendations which cryptographic standards are (un)safe to use.
So I would prefer a cover design that generally "feels" more as cryptanalysis than "hacking".
The biggest result in my thesis is the following.
Secure websites are secured using digital certificates.
These digital certificates contain the web domain name and the server's public-key and are digitally signed by a Certificate Authority (a company/government that only signs if the public-key really belongs to the owner of the web domain).
Only a few hundred Certification Authorities are trusted in web browsers and these are publically available.
Any digital certificate signed by such a Certification Authority is considered legitimate.
To fake a secure website you thus have to get a certificate containing your public-key in combination with the target domain name signed by a Certification Authority.
Our team was able to construct a rogue sub-Certification Authority, i.e.,
a Certification Authority that is authorized by one of the publicly known Certification Authorities.
Using our rogue Certification Authority we can thus create digital certificates at will for any secure website containing our public-key.
More detailed information is available at
http://www.dep.kvl.nl/trellisbox/side-ab/
An idea of the techniques in my thesis:
I look at the internal computation of a digital signature for a certificate at bit-level and compare two such computations.
A difference between two certificates will lead to differences between the two internal computations of their digital signatures and finally to two different signatures.
However, we actively adapt the certificates to control the flow of these internal differences until we find two different certificates that actually result in the same digital signature, this is called a _collision_.
Evidently, my thesis is very technical and I have tried here to provide a short description.
You can always contact me for questions and/or more detailed explanations.
Project Deadline Extended
Reason: Almost all designs focus on the very general topic of digital security (digital fingerprint, etc).
I am looking more for a design that reflects more on the topic of the thesis: attacks on hash functions.
Several ideas have already been given in the brief and discussion.
Since the old deadline is already tomorrow, I am extend it.

```html
<!DOCTYPE html>
<html lang="en">
<head>
<meta charset="utf-8">
<title>Pathways through Lattice Ciphers and Their Uses — Cover</title>
<link rel="stylesheet" href="https://fonts.googleapis.com/css2?family=Yanone+Kaffeesatz:wght@300;400&display=swap">
<style>
  :root {
    --page: #ffffff;
    --cover: #4a4a4a;
    --ink-light: #ebe6d6;
    --gold: #d9b84a;
    --rule: #a8903e;
    --disc: #f7efc6;
    --disc-ink: #4a4a4a;
  }
  * { margin: 0; padding: 0; box-sizing: border-box; }
  html, body { width: 1200px; height: 848px; overflow: hidden; background: var(--page); }
  body { position: relative; font-family: "Yanone Kaffeesatz", "Arial Narrow", sans-serif; font-weight: 300; }

  .cover { position: absolute; left: 119px; top: 93px; width: 950px; height: 656px; background: var(--cover); }
  .cover-rules { position: absolute; left: 0; top: 0; width: 1200px; height: 848px; }

  .front-title { position: absolute; left: 640px; top: 126px; color: var(--ink-light); font-size: 21px; font-weight: 300; line-height: 29px; }
  .front-author { position: absolute; left: 748px; top: 584px; color: var(--ink-light); font-size: 22px; font-weight: 300; }

  .keywords { position: absolute; left: 897px; top: 553px; list-style: none; color: var(--disc-ink); font-size: 9.5px; font-weight: 300; line-height: 20.5px; white-space: nowrap; }

  .spine-author, .spine-title, .spine-imprint {
    position: absolute; writing-mode: vertical-rl; white-space: nowrap; font-weight: 300;
  }
  .spine-author { left: 587px; top: 130px; color: var(--ink-light); font-size: 13px; }
  .spine-title { left: 566px; top: 205px; color: var(--gold); font-size: 13px; }
  .spine-imprint { left: 588px; top: 696px; color: var(--rule); font-size: 11px; }

  .back-imprint { position: absolute; left: 498px; top: 128px; color: var(--rule); font-size: 15px; font-weight: 400; }
  .back-author { position: absolute; left: 388px; top: 592px; color: var(--ink-light); font-size: 12px; font-weight: 300; }
  .back-title { position: absolute; left: 210px; top: 629px; color: var(--gold); font-size: 12px; font-weight: 300; }
</style>
</head>
<body>
  <div class="cover"></div>

  <svg class="cover-rules" viewBox="0 0 1200 848" aria-hidden="true">
    <g fill="none" stroke="var(--rule)" stroke-width="1">
      <line x1="119" y1="614" x2="1069" y2="614"/>
      <line x1="119" y1="402" x2="544" y2="749"/>
      <polyline points="119,459 155,623 1038,623 1069,473"/>
      <line x1="1069" y1="407" x2="878" y2="551"/>
      <line x1="736" y1="116" x2="736" y2="537"/>
    </g>
    <circle cx="944" cy="611" r="85" fill="var(--disc)"/>
  </svg>

  <!-- Back cover -->
  <div class="back-imprint">Kestrel Press</div>
  <div class="back-author">Joost Verhagel</div>
  <div class="back-title">Pathways through Lattice Ciphers and Their Uses</div>

  <!-- Spine -->
  <div class="spine-author">Joost Verhagel</div>
  <div class="spine-title">Pathways through Lattice Ciphers and Their Uses</div>
  <div class="spine-imprint">Kestrel Press</div>

  <!-- Front cover -->
  <h1 class="front-title">Pathways<br>through<br>Lattice<br>Ciphers<br>and Their<br>Uses</h1>
  <div class="front-author">Joost Verhagel</div>
  <ul class="keywords">
    <li>Cryptanalysis</li>
    <li>Digital fingerprint</li>
    <li>Digital signature</li>
    <li>Digital certificate</li>
    <li>Collision of fingerprint/signature</li>
    <li>Bit-difference</li>
  </ul>
</body>
</html>
```